E-book named 'Lanterns Over Marrowby: Building Kinder Firms' needs cover

I need a cover for my ebook and also paper back book.
I need a very appealing cover for my ebook. Social enterprise is a company that gives something back to the society as opposed to only make profit.
The society and its people always benefit.
So far the above is the name chosen but I welcome small changes and ideas also a tag line would also be great something like “everything you need to know to sep up a social enterprise and succeed”
I want to write in the cover something to make people buy it. I want the name Social Enterprise in more evidence ...
Target Market(s)
Students, graduates and business minded people who are thinking of set up a social enterprise company and needs guidance
Industry/Entity Type
It Company
Colors
Designer to choose colors to be used in the design.
Look and feel
Each slider illustrates characteristics of the customer's brand and the style your logo design should communicate.

```html
<!DOCTYPE html>
<html lang="en">
<head>
<meta charset="utf-8">
<title>Lanterns Over Marrowby: Building Kinder Firms — Book Cover</title>
<link rel="stylesheet" href="https://fonts.googleapis.com/css2?family=Montserrat:wght@300;500;700&family=Oswald:wght@700&display=swap">
<style>
  :root {
    --title-red: #c4262e;
    --author-band: #4d4d4d;
    --tagline-band: #13305c;
    --paper: #ffffff;
    --ink-light: #ffffff;
    --photo-sky: #f4f6f9;
    --photo-blue: #2b4f8c;
    --photo-green: #4a7a55;
    --photo-skin: #c99473;
    --photo-skin-light: #e6c3a6;
  }
  html, body {
    margin: 0;
    padding: 0;
    overflow: hidden;
    background: var(--paper);
  }
  .cover {
    position: relative;
    width: 801px;
    height: 1200px;
    overflow: hidden;
    background: var(--paper);
  }
  .title {
    position: absolute;
    left: 0;
    top: 0;
    width: 801px;
    height: 290px;
    margin: 0;
  }
  .title-kicker {
    font-family: "Montserrat", sans-serif;
    font-weight: 700;
    fill: var(--title-red);
  }
  .title-main {
    font-family: "Oswald", sans-serif;
    font-weight: 700;
    fill: var(--title-red);
  }
  .author-band {
    position: absolute;
    left: 0;
    top: 308px;
    width: 801px;
    height: 65px;
    background: var(--author-band);
  }
  .author-name {
    font-family: "Montserrat", sans-serif;
    font-weight: 500;
    fill: var(--ink-light);
  }
  .hero-art {
    position: absolute;
    left: 0;
    top: 373px;
    width: 801px;
    height: 653px;
    background: linear-gradient(180deg,
      var(--paper) 0%,
      var(--photo-sky) 10%,
      var(--photo-blue) 32%,
      var(--photo-green) 50%,
      var(--photo-skin) 72%,
      var(--photo-skin-light) 100%);
  }
  .tagline-band {
    position: absolute;
    left: 0;
    top: 1026px;
    width: 801px;
    height: 174px;
    background: var(--tagline-band);
  }
  .tagline {
    font-family: "Montserrat", sans-serif;
    font-weight: 300;
    fill: var(--ink-light);
  }
</style>
</head>
<body>
  <main class="cover">
    <h1 class="title" aria-label="Lanterns Over Marrowby: Building Kinder Firms">
      <svg width="801" height="290" viewBox="0 0 801 290" aria-hidden="true">
        <text class="title-kicker" x="34" y="124" font-size="51" textLength="736" lengthAdjust="spacingAndGlyphs">LANTERNS OVER MARROWBY:</text>
        <text class="title-main" x="34" y="266" font-size="152" textLength="736" lengthAdjust="spacingAndGlyphs">BUILDING KINDER FIRMS</text>
      </svg>
    </h1>

    <div class="author-band">
      <svg width="801" height="65" viewBox="0 0 801 65" aria-label="Marisol Quenby">
        <text class="author-name" x="401" y="50" font-size="48" text-anchor="middle" textLength="474" lengthAdjust="spacingAndGlyphs">MARISOL QUENBY</text>
      </svg>
    </div>

    <div class="hero-art" role="img" aria-label="Photograph of many children's hands reaching up together to hold a globe of the Earth showing the Americas"></div>

    <div class="tagline-band">
      <svg width="801" height="174" viewBox="0 0 801 174" aria-label="Everything you need to know to set up a social enterprise ...and succeed!">
        <text class="tagline" x="398" y="56" font-size="45" text-anchor="middle" textLength="704" lengthAdjust="spacingAndGlyphs">EVERYTHING YOU NEED TO KNOW</text>
        <text class="tagline" x="399" y="104" font-size="45" text-anchor="middle" textLength="699" lengthAdjust="spacingAndGlyphs">TO SET UP A SOCIAL ENTERPRISE</text>
        <text class="tagline" x="399" y="153" font-size="45" text-anchor="middle" textLength="338" lengthAdjust="spacingAndGlyphs">...AND SUCCEED!</text>
      </svg>
    </div>
  </main>
</body>
</html>
```